Emergency Dental Referral Company

I need a brochure to advertise my business to prospective dentists that may want to join or to dentists that may want to use this for their own patients. I also need to advertise this brochure to ER physicians who see many dental emergencies. This brochure is meant to be dual purpose: advertise our company and services to the ER physicians who then hand out the brochures to the dental emergency patients in pain. See our website for further details at www.molarquickfix.com

I will also be attaching our logo design.

Target Market(s)

Emergency Room physicians and other medical personnel who will distribute these brochures to patients in dental pain and dental emergencies

Industry/Entity Type

Business

Font styles to use
Serif
Sans Serif

Requirements
Must have
• Must be simple! Must have a call to action- inspiration to go to website. Highlight our guarantee that states "If you are not seen by a dentist in 24 hours or less, you will receive your money back. Emphasis on the logo. Must discuss how we find a dentist in your zip code in three easy steps.
• For the color- please make similar to our website of www.molarquickfix.com
Nice to have
• Would like to state that this service can see patients at any hour of the day.
Should not have
• no contact information besides the URL. www.molarquickfix.com

```html
<!DOCTYPE html>
<html lang="en">
<head>
<meta charset="utf-8">
<title>Molar Quick Fix Brochure</title>
<link href="https://fonts.googleapis.com/css2?family=Oswald:wght@500;700&family=Open+Sans:wght@400;600;700&display=swap" rel="stylesheet">
<style>
:root{
  --backdrop:#2b2b2c;
  --paper:#ffffff;
  --blue:#1a73d9;
  --blue-deep:#0d5fc0;
  --green:#3bb54a;
  --ink:#3a3a3a;
  --grey:#6b6b6b;
  --field:#c9dff5;
}
*{margin:0;padding:0;box-sizing:border-box}
html,body{width:824px;height:1200px;overflow:hidden;background:var(--backdrop)}
body{position:relative;font-family:"Open Sans",Arial,sans-serif;color:var(--ink)}
.sheet{position:absolute;background:var(--paper);overflow:hidden;box-shadow:0 6px 18px rgba(0,0,0,.5)}
.sheet--outside{left:65px;top:68px;width:701px;height:497px}
.sheet--inside{left:65px;top:616px;width:704px;height:503px}
.panel{position:absolute;top:0;height:100%}

/* outside: steps panel */
.panel--steps{left:0;width:239px}
.step{position:absolute;left:0;width:239px;text-align:center}
.step__title{font-family:"Oswald",sans-serif;font-weight:700;font-size:29px;color:var(--green);line-height:1;display:flex;justify-content:center;align-items:center;gap:6px}
.step__title svg{width:26px;height:22px}
.step__desc{font-size:17px;color:var(--grey);font-weight:600;margin-top:4px}
.pill{position:absolute;left:27px;top:214px;width:186px;height:28px;border-radius:14px;background:var(--blue);color:#fff;font-weight:700;font-size:19px;text-align:center;line-height:28px}
.about{position:absolute;left:18px;top:254px;width:208px;font-size:8.8px;line-height:11.6px;color:#555;letter-spacing:-.1px}
.about p+p{margin-top:9px}

/* outside: middle panel */
.panel--cover{left:239px;width:230px;background:linear-gradient(180deg,var(--blue) 0%,var(--blue-deep) 100%)}
.cover__flag{position:absolute;left:0;top:0;width:230px;height:190px}
.brand{display:flex;align-items:center;justify-content:center;gap:6px;font-weight:700;color:var(--blue);font-size:16px;line-height:1.1}
.brand__dot{width:22px;height:22px;border-radius:50%;background:var(--blue);flex:none}
.cover__brand{position:absolute;left:0;top:55px;width:230px}
.cover__url{position:absolute;left:0;top:214px;width:230px;text-align:center;color:#fff;font-weight:700;font-size:16.5px}
.cover__photo{position:absolute;left:0;top:250px;width:230px;height:247px;background:linear-gradient(160deg,#3e9cf0 0%,#1f6fd0 60%,#0f55b0 100%)}

/* outside: right panel */
.panel--promise{left:469px;width:232px}
.promise__brand{position:absolute;left:0;top:48px;width:232px;font-size:17px}
.promise__text{position:absolute;left:14px;top:122px;width:204px;text-align:center;color:var(--blue);font-weight:700;font-size:12.4px;line-height:15px}
.promise__art{position:absolute;left:0;top:0;width:232px;height:497px}

/* inside: form panel */
.panel--form{left:0;width:239px}
.form__head{position:absolute;left:0;top:12px;width:239px;display:flex;justify-content:center;align-items:center;gap:6px;font-family:"Oswald",sans-serif;font-weight:700;font-size:29px;color:var(--blue);line-height:1}
.form__head svg{width:26px;height:22px}
.bar{position:absolute;left:27px;width:204px;background:var(--green);color:#fff;font-weight:700;text-align:center}
.bar--start{top:50px;height:19px;font-size:14px;line-height:19px}
.bar--dob{top:163px;height:19px;font-size:15px;line-height:19px}
.bar--contact{top:220px;height:19px;font-size:14px;line-height:19px}
.form__step{position:absolute;left:27px;top:76px;width:204px;display:flex;align-items:center;justify-content:center;gap:8px;font-family:"Oswald",sans-serif;font-weight:700;font-size:24px;color:var(--blue)}
.form__step i{display:block;width:38px;height:2px;background:var(--blue)}
.field{position:absolute;left:17px;width:214px;height:21px;border:1px solid var(--field);font-size:12px;font-weight:700;color:var(--blue);padding-left:5px;line-height:19px}
.chips{position:absolute;left:17px;width:214px;display:flex;justify-content:space-between}
.chip{width:64px;height:19px;border:1px solid var(--field);font-size:12px;font-weight:700;color:var(--blue);text-align:center;line-height:17px}
.notice{position:absolute;left:20px;top:278px;width:206px;text-align:center;font-size:9.2px;font-weight:700;color:var(--grey);line-height:13.5px}
.callbox{position:absolute;left:57px;top:340px;width:139px;height:20px;border:1px solid var(--field);font-size:12px;font-weight:700;color:var(--blue);text-align:center;line-height:18px}

/* inside: decor & right side */
.inside__decor{position:absolute;left:0;top:0;width:704px;height:503px}
.inside__photo{position:absolute;left:239px;top:0;width:243px;height:195px;background:linear-gradient(135deg,#dfe9f2 0%,#e9c3ac 45%,#c98d74 70%,#9fb9cf 100%)}
.copy{position:absolute;font-size:10.4px;line-height:13.6px}
.copy--mid{left:255px;top:198px;width:214px;color:#333}
.copy--top{left:489px;top:8px;width:208px;text-align:right;color:#333}
.copy--low{left:489px;top:330px;width:208px;text-align:center;color:#fff}
.round-photo{position:absolute;left:485px;top:157px;width:128px;height:128px;border-radius:50%;border:5px solid var(--blue);background:radial-gradient(circle at 45% 40%,#f0d3bf 0%,#c8dff2 55%,#6ea9dd 100%)}
.inside__brand{position:absolute;left:290px;top:415px;width:190px;font-size:15px}
.inside__brand .brand__dot{background:#fff}
.inside__brand .brand{color:#fff}
.inside__url{position:absolute;left:160px;top:470px;width:330px;text-align:center;color:#fff;font-weight:700;font-size:16px}
</style>
</head>
<body>

<section class="sheet sheet--outside">
  <div class="panel panel--steps">
    <div class="step" style="top:26px">
      <div class="step__title"><svg viewBox="0 0 26 22"><path d="M2 11 L10 19 L24 3" fill="none" stroke="#1a73d9" stroke-width="5" stroke-linecap="round"/></svg>Step 1</div>
      <div class="step__desc">Fill out a frorm</div>
    </div>
    <div class="step" style="top:92px">
      <div class="step__title"><svg viewBox="0 0 26 22"><path d="M2 11 L10 19 L24 3" fill="none" stroke="#1a73d9" stroke-width="5" stroke-linecap="round"/></svg>Step 2</div>
      <div class="step__desc">Find a Dentist</div>
    </div>
    <div class="step" style="top:157px">
      <div class="step__title"><svg viewBox="0 0 26 22"><path d="M2 11 L10 19 L24 3" fill="none" stroke="#1a73d9" stroke-width="5" stroke-linecap="round"/></svg>Step 3</div>
      <div class="step__desc">Get your appoinment</div>
    </div>
    <div class="pill">About Us</div>
    <div class="about">
      <p>Our mission plain and simple is to get you seen by a qualified dentist as quickly as possible to get you out of pain. Nobody likes pain and no one should have to live with it. If we can get you seen by a dentist in 24 hours or less, we have succeeded.</p>
      <p>What we strive for is a quicker, more reliable method for patients to access their dental professional. Going to the local hospitals' Emergency Department for a tooth ache will not solve the issue, hospitals are often times not equipped to handle dental emergencies and do not have dentists on staff. You leave with antibiotics and pain medication, not a solution to the real underlying problem. Leave here confident, knowing you will see a dentist in less than 24 hours!</p>
    </div>
  </div>

  <div class="panel panel--cover">
    <svg class="cover__flag" viewBox="0 0 230 190"><polygon points="22,0 208,0 208,160 115,190 22,160" fill="#ffffff"/></svg>
    <div class="cover__brand"><div class="brand"><span class="brand__dot"></span>Molar Quick Fix</div></div>
    <div class="cover__url">www.molarquickfix.com</div>
    <div class="cover__photo" role="img" aria-label="Photo of a dentist treating a patient, in blue tones"></div>
  </div>

  <div class="panel panel--promise">
    <svg class="promise__art" viewBox="0 0 232 497">
      <defs>
        <linearGradient id="chairPhoto" x1="0" y1="0" x2="1" y2="1">
          <stop offset="0" stop-color="#f1ddd0"/>
          <stop offset=".5" stop-color="#d9a48c"/>
          <stop offset="1" stop-color="#efe9e6"/>
        </linearGradient>
      </defs>
      <polygon points="0,262 86,345 232,196 232,497 0,497" fill="url(#chairPhoto)" role="img" aria-label="Photo of a patient in protective glasses receiving dental treatment"/>
      <polyline points="-4,250 86,340 236,188" fill="none" stroke="#ffffff" stroke-width="42" stroke-linejoin="miter"/>
      <polyline points="-4,250 86,340 236,188" fill="none" stroke="#3bb54a" stroke-width="30" stroke-linejoin="miter"/>
    </svg>
    <div class="promise__brand"><div class="brand"><span class="brand__dot"></span>Molar Quick Fix</div></div>
    <div class="promise__text">If you are not seen by a dentist in 24 hours or less, you will receive your money back.</div>
  </div>
</section>

<section class="sheet sheet--inside">
  <svg class="inside__decor" viewBox="0 0 704 503">
    <polygon points="0,340 250,430 704,170 704,210 250,470 0,375" fill="#1a73d9"/>
    <polygon points="250,470 704,210 704,503 180,503" fill="#3bb54a"/>
    <polygon points="0,392 250,487 270,476 0,384" fill="#1a73d9"/>
  </svg>

  <div class="panel panel--form">
    <div class="form__head"><svg viewBox="0 0 26 22"><path d="M2 11 L10 19 L24 3" fill="none" stroke="#3bb54a" stroke-width="5" stroke-linecap="round"/></svg>Find a Dentist</div>
    <div class="bar bar--start">Get Started</div>
    <div class="form__step"><i></i>Step 1<i></i></div>
    <div class="field" style="top:107px">Name</div>
    <div class="field" style="top:135px">Last</div>
    <div class="bar bar--dob">Date of Birth</div>
    <div class="chips" style="top:190px"><span class="chip">Month</span><span class="chip">Day</span><span class="chip">Year</span></div>
    <div class="bar bar--contact">Preferred contact method</div>
    <div class="chips" style="top:249px"><span class="chip">Phone</span><span class="chip">Email</span><span class="chip">Text</span></div>
    <div class="notice">IF YOU DO NOT PROVIDE A VALID PHONE NUMBER OR EMAIL ADDRESS WE CANNOT CONTACT YOU AND THEREFORE CANNOT SCHEDULE YOUR APPOINTMENT</div>
    <div class="callbox">Call Phone</div>
  </div>

  <div class="inside__photo" role="img" aria-label="Photo of a dentist examining a smiling patient"></div>
  <p class="copy copy--mid">Lorem Ipsum is simply dummy text of the printing and typesetting industry. Lorem Ipsum has been the industry's standard dummy text ever since the 1500s, when an unknown printer took a galley of type and scrambled it to mak Lorem Ipsum is simply dummy text of the printing and</p>
  <p class="copy copy--top">Lorem Ipsum is simply dummy text of the printing and typesetting industry. Lorem Ipsum has been the industry's standard dummy text ever since the 1500s, when an unknown printer took a galley of type and scrambled it text of the printing and to mak Lorem Ipsum is simply dummy Ipsum is simply dummy Ipsum is simply dummy</p>
  <div class="round-photo" role="img" aria-label="Round photo of a child at a dental checkup"></div>
  <p class="copy copy--low">Lorem Ipsum is simply dummy text of the printing and typesetting industry. Lorem Ipsum has been the industry's standard dummy text ever since the 1500s, when an unknown printer took a galley of type and scrambled it text of the printing and to mak Lorem Ipsum is simply dummy Ipsum is simply dummy Ipsum is simply dummy Lorem Ipsum is simply dummy</p>
  <div class="inside__brand"><div class="brand"><span class="brand__dot"></span>Molar Quick Fix</div></div>
  <div class="inside__url">www.molarquickfix.com</div>
</section>

</body>
</html>
```